Health IT software startup needs a product sheet to promote our software/company

-Need a one page product sheet that highlights our software and company for our customers.
-Our software is an EHR (electronic health record) software for hospitals.
-Attached is our logo (2 options-picture 4,5). Our caption with the logo should read "An EHR developed by physicians and healthcare professionals with decades of experience in behavioral health".
-Incorporate another smaller sub-heading (section) in the product sheet- titled "How Mendora Helps You"- with three associated words- 'Quality, Familiarity, Security'.
-Incorporate the main section titled "Our Software" with a description of the software with 3 components to use- see attached word document- Mendora Product Sheet.
-Attached is a optional photo you may consider if you like- we currently use it on our website with our logo and logo caption- see attached homepage-resized.jpg
-you can additional royalty free photos as needed
-Finally, the 'Contact Us' information:
404-612-8350
info@mendorasoftware.example
www.mendorasoftware.example

Target Market(s)

Behavioral Health Hospitals- specifically the product sheet will be left with the customers after we demo the software to them.

Font styles to use
Serif
Sans Serif

Colors
0555a3
3276b5
85acd3
0393ce
33a6d7
00a990
cedeed
ecf7fb
33b8a4

Requirements
Should not have
• Please do not saturate the product sheet with only colors- utilize white space

```html
<!DOCTYPE html>
<html lang="en">
<head>
<meta charset="utf-8">
<title>Mendora Product Sheet</title>
<link rel="stylesheet" href="https://fonts.googleapis.com/css2?family=Open+Sans:wght@400;700;800&family=Arimo:wght@400&display=swap">
<style>
  :root {
    --stage: #f4dbb0;
    --paper: #ffffff;
    --teal: #63c8d6;
    --teal-band: #3dbccb;
    --teal-text: #1897a6;
    --navy: #1f3f8e;
    --ink: #1b1b1b;
    --mist: #eef6f9;
    --card: #dedede;
    --shadow: #d4d4d4;
    --photo-a: #f1f4f5;
    --photo-b: #c9d9e0;
  }
  * { box-sizing: border-box; margin: 0; padding: 0; }
  html, body { width: 1200px; height: 800px; overflow: hidden; background: var(--stage); }
  .sheet {
    position: absolute; left: 343px; top: 20px;
    width: 514px; height: 760px;
    background: var(--paper);
    font-family: "Arimo", Arial, sans-serif;
    box-shadow: 4px 6px 14px rgba(0,0,0,0.18);
    overflow: hidden;
  }
  .intro-panel { position: absolute; left: 0; top: 34px; width: 234px; height: 230px; background: var(--mist); }
  .hero-photo {
    position: absolute; left: 234px; top: 34px; width: 280px; height: 211px;
    background: linear-gradient(100deg, var(--photo-a) 0%, var(--photo-b) 55%, #e6ecee 100%);
  }
  .hero-band { position: absolute; left: 232px; top: 245px; width: 282px; height: 20px; background: var(--teal-band); }
  .brand { position: absolute; left: 14px; top: 58px; display: flex; align-items: center; gap: 7px; }
  .brand-dot { width: 22px; height: 22px; border-radius: 50%; background: var(--navy); }
  .brand-name { font-family: "Open Sans", sans-serif; font-weight: 400; font-size: 20px; color: var(--navy); }
  .tagline {
    position: absolute; left: 15px; top: 94px;
    font-size: 11.5px; line-height: 25px; letter-spacing: 0.9px;
    color: var(--teal-text); text-transform: uppercase; white-space: nowrap;
  }
  .helps-shape { position: absolute; left: 0; top: 265px; }
  .helps-title {
    position: absolute; left: 57px; top: 294px;
    font-family: "Open Sans", sans-serif; font-weight: 800;
    font-size: 20px; line-height: 25px; letter-spacing: 1.3px; color: var(--ink);
  }
  .values {
    position: absolute; left: 322px; top: 289px; list-style: none;
    font-family: "Open Sans", sans-serif; font-weight: 800;
    font-size: 20px; line-height: 35px; letter-spacing: 1.2px; color: var(--ink);
    white-space: nowrap;
  }
  .product-label {
    position: absolute; left: 181px; top: 427px; width: 162px; height: 29px;
    background: var(--teal); color: #fff;
    font-family: "Open Sans", sans-serif; font-weight: 700; font-size: 16px; letter-spacing: 1.5px;
    display: flex; align-items: center; justify-content: center;
  }
  .feature-title {
    position: absolute; top: 464px;
    font-family: "Open Sans", sans-serif; font-weight: 800;
    font-size: 15px; line-height: 16px; letter-spacing: 0.9px; color: var(--teal-text);
    white-space: nowrap;
  }
  .feature-text {
    position: absolute; background: var(--card); color: var(--ink);
    font-size: 11.5px; letter-spacing: 0.7px; text-transform: uppercase;
    padding: 9px 4px 0 12px; white-space: nowrap; overflow: hidden;
  }
  .organic { left: 8px; top: 504px; width: 159px; height: 188px; line-height: 19.4px; }
  .engagement { left: 173px; top: 502px; width: 159px; height: 189px; line-height: 25px; padding-left: 5px; padding-top: 7px; }
  .risk { left: 340px; top: 505px; width: 165px; height: 186px; line-height: 16.9px; padding-left: 8px; padding-top: 6px; }
  .contact {
    position: absolute; left: 0; top: 706px; width: 514px; height: 54px;
    background: var(--teal); color: #fff;
    font-size: 20px; letter-spacing: 2px;
    display: flex; align-items: center; padding-left: 22px; gap: 18px;
  }
</style>
</head>
<body>
  <main class="sheet">
    <div class="intro-panel"></div>
    <div class="hero-photo" role="img" aria-label="Photo of a physical therapist helping a smiling patient raise her arm"></div>
    <div class="hero-band"></div>

    <div class="brand">
      <span class="brand-dot"></span>
      <span class="brand-name">Mendora</span>
    </div>
    <p class="tagline">"An EHR developed by<br>physicians and<br>healthcare profes-<br>sionals with decades<br>of experience in be-<br>havioral health"</p>

    <svg class="helps-shape" width="300" height="156" viewBox="0 0 300 156" aria-hidden="true">
      <rect x="0" y="142" width="297" height="14" fill="var(--shadow)"/>
      <polygon points="0,0 238,0 297,142 0,142" fill="var(--teal)"/>
    </svg>
    <h2 class="helps-title">HOW<br>MENDORA<br>HELPS YOU</h2>
    <ol class="values">
      <li>1. QUALITY</li>
      <li>2. FAMILIARITY</li>
      <li>3. SECURITY</li>
    </ol>

    <div class="product-label">OUR PRODUCT</div>

    <h3 class="feature-title" style="left:12px">ORGANIC<br>DOCUMENTATION</h3>
    <h3 class="feature-title" style="left:192px;top:463px">PATIENT<br>ENGAGEMENT</h3>
    <h3 class="feature-title" style="left:359px;top:465px">RISK<br>MANAGEMENT</h3>

    <p class="feature-text organic">Mendora set out<br>to provide behav-<br>ioral health clini-<br>cians a familiar<br>platform to<br>engage in chart<br>level documenta-<br>tion for their pa-<br>tient care.</p>
    <p class="feature-text engagement">Using our propri-<br>etary Mendora<br>modules, we seam-<br>lessly digitalize<br>therapy for use in<br>both individual and<br>group therapy.</p>
    <p class="feature-text risk">To facilitate and<br>navigate the ev-<br>er-changing regu-<br>latory environ-<br>ment, Mendora<br>built tailored risk<br>management/quali-<br>ty improvement ca-<br>pabilities into the<br>software.</p>

    <footer class="contact"><span>CONTACT US</span><span>404-612-8350</span></footer>
  </main>
</body>
</html>
```